Regenerative Wellness Flyer to recruit Dr offices and clinics

This is a flyer that will be used to recruit new Dr offices and clinics to make them aware of a brand new product that is about to hit the market.

I uploaded an older flyer that I do like. This product is not Stem Cells but fixes a lot of the same things. So the title could be Regenerative Wellness and Cell Factor Therapy.

I also loaded a multiple page info on the product.

I would like to be able to change out logo's & contact information as I have a couple sales people helping push this. I also attached my logo, Velmora. Would like to be able to a QR code...

This is the landing page that the flyer will drive Dr's to:
https://app.pagebrixel.com/v2/preview/K3QwzRtuNaLmBv8Hp2Dx?notrack=true

Target Market(s)

Dr's office, clinics, alternative wellness clinics

Industry/Entity Type

health & wellness

Colors
0054AA
0677BA
7BADD7
CADEEF
E8F1F8
00AB8E
00BBA5
67D7C9
C6EFE9
E9F9F6

Requirements
Nice to have
• The ability to change out the logo/contact info areas

```html
<!DOCTYPE html>
<html lang="en">
<head>
<meta charset="utf-8">
<title>Velmora Wellness – Regenerative Wellness &amp; Cell Factor Therapy</title>
<link rel="stylesheet" href="https://fonts.googleapis.com/css2?family=Poppins:wght@400;500;600;700;800&display=swap">
<style>
  :root{
    --navy:#0054AA;
    --blue:#0677BA;
    --sky:#7BADD7;
    --mist:#CADEEF;
    --ice:#E8F1F8;
    --green:#00AB8E;
    --teal:#00BBA5;
    --aqua:#67D7C9;
    --foam:#C6EFE9;
    --pale:#E9F9F6;
    --ink:#2f3a44;
    --black:#111;
    --white:#fff;
  }
  *{margin:0;padding:0;box-sizing:border-box}
  html,body{width:818px;height:1200px;overflow:hidden;background:var(--white)}
  body{font-family:'Poppins',sans-serif;color:var(--ink);position:relative}
  .abs{position:absolute}

  .hero-shapes{position:absolute;left:0;top:0;width:818px;height:500px}

  .doctor-photo{left:75px;top:50px;width:349px;height:310px;border-radius:46px 46px 0 46px;
    background:linear-gradient(160deg,var(--teal),var(--blue))}
  .family-photo{left:465px;top:232px;width:283px;height:227px;border-radius:14px 40px 40px 40px;
    background:linear-gradient(135deg,#5f6b55,#c9c2b4)}

  .brand-name{left:525px;top:182px;width:253px;text-align:center;color:var(--white);
    font-weight:800;font-size:17px;line-height:1.1}
  .brand-tagline{left:525px;top:203px;width:253px;text-align:center;color:var(--white);
    font-weight:500;font-size:7.5px;letter-spacing:1.6px;text-transform:uppercase}

  .heading{left:52px;line-height:1}
  .heading .accent{color:var(--blue);font-weight:800;display:block}
  .heading .rest{color:var(--ink);font-weight:400;display:block}
  .rule{position:absolute;left:52px;height:1.5px;background:var(--black)}

  .conditions{top:400px;font-size:32px}
  .conditions .rest{font-size:28px;margin-top:4px}

  .condition-list{list-style:none;position:absolute;top:483px;width:300px}
  .condition-list li{display:flex;align-items:center;height:27.4px;font-size:19px;white-space:nowrap}
  .condition-list svg{width:20px;height:20px;margin-right:15px;flex:none}
  .col-a{left:53px}
  .col-b{left:306px}

  .section-title{font-size:31px}
  .section-title .rest{margin-top:1px}
  .body-copy{position:absolute;left:52px;width:420px;font-size:16.6px;line-height:22px;color:var(--black)}

  .divider{left:490px;top:665px;width:1.5px;height:473px;background:var(--black)}

  .qr-slot{left:588px;top:680px;width:130px;height:130px;border-radius:8px;
    background:var(--ice);border:2px solid var(--sky)}
  .qr-caption{left:505px;top:818px;width:296px;text-align:center;font-size:12px;font-weight:600;color:var(--blue)}

  .cta{left:505px;top:846px;width:296px;text-align:center;font-weight:800;font-size:15.2px;
    line-height:22px;color:var(--black);text-transform:uppercase}

  .contact{left:515px;top:935px;width:276px;text-align:center;font-size:13px;line-height:20px;color:var(--ink)}
  .contact .label{font-size:10px;font-weight:700;letter-spacing:1.4px;color:var(--green);text-transform:uppercase}
  .contact .name{font-size:17px;font-weight:700;color:var(--navy);line-height:26px}
  .contact .url{margin-top:6px;font-size:9.5px;line-height:13px;color:var(--blue);word-break:break-all}

  .footer-band{left:0;top:1166px;width:818px;height:34px;background:var(--navy)}
</style>
</head>
<body>

<svg class="hero-shapes" viewBox="0 0 818 500" aria-hidden="true">
  <path d="M525 0H818V493H612Q570 485 545 455L525 225Z" fill="var(--aqua)"/>
  <circle cx="651" cy="108" r="70" fill="var(--pale)"/>
  <path d="M117 39H378Q434 39 434 95V368H117Q65 368 65 316V91Q65 39 117 39Z" fill="var(--white)" stroke="var(--sky)" stroke-width="2"/>
  <path d="M525 225H710Q755 225 755 270V420Q755 466 710 466H500Q458 466 458 424V232Z" fill="var(--white)"/>
  <path d="M49 43h8v9h9v8h-9v9h-8v-9h-9v-8h9z" fill="none" stroke="var(--teal)" stroke-width="2" stroke-linejoin="round"/>
  <path d="M470 74h8v9h9v8h-9v9h-8v-9h-9v-8h9z" fill="none" stroke="var(--teal)" stroke-width="2" stroke-linejoin="round"/>
  <rect x="457" y="133" width="52" height="52" rx="10" fill="var(--blue)"/>
  <path d="M483 173c-9-6-14-10.5-14-16a7 7 0 0 1 14-2a7 7 0 0 1 14 2c0 5.5-5 10-14 16z" fill="var(--white)"/>
  <path d="M750 457h9l4-7 5 14 5-20 4 19 3-6h13" fill="none" stroke="var(--white)" stroke-width="1.6" stroke-linejoin="round"/>
</svg>

<div class="abs doctor-photo" role="img" aria-label="Photo of a smiling doctor in scrubs with a stethoscope"></div>
<div class="abs family-photo" role="img" aria-label="Photo of a happy family lifting their little daughter outdoors"></div>

<div class="abs brand-name">Velmora Wellness</div>
<div class="abs brand-tagline">Regenerative Wellness</div>

<h2 class="abs heading conditions">
  <span class="accent">CONDITIONS CELL</span>
  <span class="rest">FACTOR THERAPY MAY HELP</span>
</h2>
<div class="rule" style="top:466px;width:356px"></div>

<ul class="condition-list col-a">
  <li><svg viewBox="0 0 20 20"><circle cx="9" cy="11" r="7.5" fill="none" stroke="var(--sky)" stroke-width="1.3"/><path d="M5 10.5l3.5 3.5L18 3" fill="none" stroke="var(--green)" stroke-width="2.6" stroke-linecap="round"/></svg>Knee Injuries</li>
  <li><svg viewBox="0 0 20 20"><circle cx="9" cy="11" r="7.5" fill="none" stroke="var(--sky)" stroke-width="1.3"/><path d="M5 10.5l3.5 3.5L18 3" fill="none" stroke="var(--green)" stroke-width="2.6" stroke-linecap="round"/></svg>Hip &amp; Labral Tears</li>
  <li><svg viewBox="0 0 20 20"><circle cx="9" cy="11" r="7.5" fill="none" stroke="var(--sky)" stroke-width="1.3"/><path d="M5 10.5l3.5 3.5L18 3" fill="none" stroke="var(--green)" stroke-width="2.6" stroke-linecap="round"/></svg>Chronic Back Pain</li>
  <li><svg viewBox="0 0 20 20"><circle cx="9" cy="11" r="7.5" fill="none" stroke="var(--sky)" stroke-width="1.3"/><path d="M5 10.5l3.5 3.5L18 3" fill="none" stroke="var(--green)" stroke-width="2.6" stroke-linecap="round"/></svg>Wrist or Elbow</li>
  <li><svg viewBox="0 0 20 20"><circle cx="9" cy="11" r="7.5" fill="none" stroke="var(--sky)" stroke-width="1.3"/><path d="M5 10.5l3.5 3.5L18 3" fill="none" stroke="var(--green)" stroke-width="2.6" stroke-linecap="round"/></svg>Ankle &amp; Foot Pain</li>
</ul>
<ul class="condition-list col-b">
  <li><svg viewBox="0 0 20 20"><circle cx="9" cy="11" r="7.5" fill="none" stroke="var(--sky)" stroke-width="1.3"/><path d="M5 10.5l3.5 3.5L18 3" fill="none" stroke="var(--green)" stroke-width="2.6" stroke-linecap="round"/></svg>Arthritis/Osteoarthritis</li>
  <li><svg viewBox="0 0 20 20"><circle cx="9" cy="11" r="7.5" fill="none" stroke="var(--sky)" stroke-width="1.3"/><path d="M5 10.5l3.5 3.5L18 3" fill="none" stroke="var(--green)" stroke-width="2.6" stroke-linecap="round"/></svg>Shoulder Damage</li>
  <li><svg viewBox="0 0 20 20"><circle cx="9" cy="11" r="7.5" fill="none" stroke="var(--sky)" stroke-width="1.3"/><path d="M5 10.5l3.5 3.5L18 3" fill="none" stroke="var(--green)" stroke-width="2.6" stroke-linecap="round"/></svg>Low Back Pain</li>
  <li><svg viewBox="0 0 20 20"><circle cx="9" cy="11" r="7.5" fill="none" stroke="var(--sky)" stroke-width="1.3"/><path d="M5 10.5l3.5 3.5L18 3" fill="none" stroke="var(--green)" stroke-width="2.6" stroke-linecap="round"/></svg>Achilles Tendon</li>
  <li><svg viewBox="0 0 20 20"><circle cx="9" cy="11" r="7.5" fill="none" stroke="var(--sky)" stroke-width="1.3"/><path d="M5 10.5l3.5 3.5L18 3" fill="none" stroke="var(--green)" stroke-width="2.6" stroke-linecap="round"/></svg>Plantar Fasciitis</li>
</ul>

<h2 class="abs heading section-title" style="top:647px;left:50px">
  <span class="accent">REGENERATE &amp;</span>
  <span class="rest">REPAIR TISSUE</span>
</h2>
<div class="rule" style="top:715px;width:199px"></div>
<p class="body-copy" style="top:725px">Cell factors are signalling proteins that wake up the body's natural repair system and help regenerate damaged tissue.</p>

<h2 class="abs heading section-title" style="top:821px">
  <span class="accent">DECREASE PAIN</span>
  <span class="rest">&amp; SORENESS</span>
</h2>
<div class="rule" style="top:888px;width:174px"></div>
<p class="body-copy" style="top:903px">Cell factors have powerful anti-inflammatory action. Reduced inflammation leads to a decrease in pain &amp; soreness in the body.</p>

<h2 class="abs heading section-title" style="top:1001px">
  <span class="accent" style="display:inline">IMPROVE YOUR</span><span class="rest" style="display:inline"> HEALTH</span>
</h2>
<div class="rule" style="top:1042px;width:355px"></div>
<p class="body-copy" style="top:1054px;left:51px">Research shows cell factor therapy may benefit a wide variety of health complications and help patients live stronger, healthier lives.</p>

<div class="abs divider"></div>

<div class="abs qr-slot" role="img" aria-label="QR code linking to the Velmora landing page"></div>
<p class="abs qr-caption">Scan to learn about Cell Factor Therapy</p>

<p class="abs cta">Capture this new opportunity<br>in your area before any<br>other clinic</p>

<div class="abs contact">
  <p class="label">Your Velmora Representative</p>
  <p class="name">Dana Whitfield</p>
  <p>(555) 014-2288</p>
  <p>dana@velmorawellness.com</p>
  <p class="url">https://app.pagebrixel.com/v2/preview/K3QwzRtuNaLmBv8Hp2Dx?notrack=true</p>
</div>

<div class="abs footer-band"></div>

</body>
</html>
```